Vellorane- Comprehensive quality healthcare delivered at your door.

I am looking for brochures to help promote my business. My business name is Vellorne (see attachment and logo). This is a new health delivery system designed to provide high quality care to elderly in their communities or at home.

See attachements. The logo is already designed.

As far as services provided (see attachment)

Target Market(s)

Elderly patients

Industry/Entity Type

Business

Font styles to use
Serif

Colors

Designer to choose colors to be used in the design.

```html
<!DOCTYPE html>
<html lang="en">
<head>
<meta charset="utf-8">
<title>Vellorne – Brochure</title>
<link href="https://fonts.googleapis.com/css2?family=Lora:wght@400;500&display=swap" rel="stylesheet">
<style>
  :root {
    --green-dark: #2c4410;
    --green-mid: #4f7a12;
    --green-bright: #7db51a;
    --orange: #f08a12;
    --orange-text: #e5621c;
    --brand-dark: #2c3814;
    --ink: #1d1d1d;
    --paper: #ffffff;
  }
  * { margin: 0; padding: 0; box-sizing: border-box; }
  html, body { width: 855px; height: 1200px; overflow: hidden; background: var(--paper); }
  .brochure {
    position: relative;
    width: 855px;
    height: 1200px;
    overflow: hidden;
    font-family: "Lora", Georgia, serif;
    color: var(--ink);
  }
  .backdrop { position: absolute; inset: 0; }

  .brand {
    position: absolute;
    left: 84px;
    top: 68px;
    width: 206px;
    text-align: center;
  }
  .brand-dot {
    display: block;
    width: 140px;
    height: 140px;
    margin: 0 auto 10px;
    border-radius: 50%;
    background: var(--orange);
  }
  .brand-name {
    font-size: 32px;
    font-weight: 400;
    letter-spacing: 0.5px;
    color: var(--brand-dark);
  }

  .nav-list {
    position: absolute;
    left: 34px;
    top: 284px;
    list-style: none;
    font-size: 16px;
    line-height: 23.3px;
    color: var(--orange-text);
  }
  .nav-list li { position: relative; padding-left: 47px; }
  .nav-list li::before {
    content: "•";
    position: absolute;
    left: 0;
    font-size: 11px;
  }

  .section-title {
    position: absolute;
    left: 31px;
    font-size: 16px;
    font-weight: 400;
    color: var(--orange-text);
  }
  .stay-title { top: 514px; }
  .services-title { top: 668px; }
  .sites-title { top: 957px; }

  .intro {
    position: absolute;
    left: 31px;
    top: 542px;
    width: 640px;
    font-size: 13.4px;
    line-height: 19.5px;
  }
  .intro p + p { margin-top: 12px; }

  .services-list {
    position: absolute;
    left: 31px;
    top: 697px;
    list-style: none;
    font-size: 13.4px;
    line-height: 20px;
  }

  .site-name {
    position: absolute;
    left: 33px;
    top: 980px;
    font-size: 13.4px;
  }

  .photo-strip {
    position: absolute;
    left: 230px;
    top: 837px;
    width: 586px;
    height: 179px;
    border: 4px solid var(--orange);
    display: flex;
    background: var(--orange);
    gap: 3px;
  }
  .photo-hands {
    flex: 0 0 321px;
    background: linear-gradient(135deg, #f4f2ee 0%, #d9c3ae 50%, #b88f72 100%);
  }
  .photo-visit {
    flex: 1;
    background: linear-gradient(120deg, #c9d3da 0%, #8a6a58 45%, #d98a9a 75%, #5b82b4 100%);
  }
</style>
</head>
<body>
<div class="brochure">
  <svg class="backdrop" width="855" height="1200" viewBox="0 0 855 1200" aria-hidden="true">
    <defs>
      <linearGradient id="greenSweep" x1="0" y1="1" x2="1" y2="0">
        <stop offset="0" stop-color="#243a0c"/>
        <stop offset="0.45" stop-color="#4f7a12"/>
        <stop offset="1" stop-color="#7db51a"/>
      </linearGradient>
    </defs>
    <rect width="855" height="1200" fill="url(#greenSweep)"/>
    <path d="M0,0 H640 C790,90 860,260 845,380 C825,580 660,760 420,890 C280,970 140,1050 0,1110 Z" fill="#f08a12"/>
    <path d="M0,0 H855 C700,12 520,40 430,70 C620,60 785,110 800,280 C815,470 690,680 440,850 C310,940 150,1020 0,1052 Z" fill="#ffffff"/>
  </svg>

  <div class="brand">
    <span class="brand-dot"></span>
    <div class="brand-name">VELLORNE</div>
  </div>

  <ul class="nav-list">
    <li>Home</li>
    <li>Assisted Living</li>
    <li>Skilled Nursing</li>
    <li>Independent Living</li>
    <li>Home and Community Based Services</li>
    <li>Respite Care</li>
    <li>Rehabilitation</li>
    <li>KAIRO LearningCenter</li>
    <li>KAIRO Learning*</li>
  </ul>

  <h2 class="section-title stay-title">STAY HOME</h2>
  <div class="intro">
    <p>Vellorne offers home and Community Based Services for adults who wish to continue to live independently in the comfort of their communities.</p>
    <p>We provide on site services and deliver high quality healthcare at your door.&nbsp; Our experienced physicians coordinate care with our certified nurse practitioners and provide chronic care management, physical therapy, rehabilitation and medications management.</p>
  </div>

  <h2 class="section-title services-title">SERVICES</h2>
  <ul class="services-list">
    <li>Comprehensive primary care services</li>
    <li>Coordination of speciality care</li>
    <li>Chronic disease management such as COPD, Asthma, Diabetes mellitus,</li>
    <li>Heart disease like congestive heart failure, Alzheimer’s dementia, etc...</li>
    <li>Transitional Care</li>
    <li>Skilled nursing visits for wound care, catheter care, ostomy</li>
    <li>Social services assessment</li>
    <li>Home health assistance</li>
    <li>Physical therapy</li>
    <li>Mental health</li>
    <li>Dental health</li>
    <li>Transportation</li>
  </ul>

  <h2 class="section-title sites-title">Sites of Operations</h2>
  <div class="site-name">Still Harbor</div>

  <div class="photo-strip">
    <div class="photo-hands" role="img" aria-label="Photo of a caregiver gently holding an elderly person's hands"></div>
    <div class="photo-visit" role="img" aria-label="Photo of a nurse visiting an elderly couple at home"></div>
  </div>
</div>
</body>
</html>
```